Brightvale Inc. Business Card Design

Brightvale Inc. is in search of a great clean design for our business cards!

Looking to incorporate our full logo and watermark on side one (however, I am open to having the text and watermark separated within the design.)

On side two, I am looking to have contact information (Name, Position, Phone #, Email, Website (www.thebrightvale.ca). Can have the logo and/or watermark as part of the design if applicable.

Please add tagline "Where Shine Counts" on either side 1 or 2. This tagline can be in a sans serif, serif or cursive font as long as it compliments overall design. Capitalization can be title or sentence case depending on how it fits within the design.

Get creative!! Looking for a clean, crisp, premium design! Looking for a glossy card finish with spot UV features when printed. Cards will also be printed with rounded corners. Standard dimensions (3.5 x 2).

Target Market(s)

B2B - primary clients are business owners or property management corporations. (residential jobs are few and far between)

Industry/Entity Type

Business

Contact Information for Business Card

- clean, crisp design
- double sided
- spot UV accents and glossy finish upon printing
- standard business card size (3.5 x 2) with rounded corners
- please see project description for requirements per side

Font styles to use
Sans Serif

Requirements
Must have
• - adequate bleeds with print ready files
• - cohesive design elements between side 1 & 2
• - spot UV elements (can be on both sides or just one, use your discretion)
• - colour pallet should match the logo file provided
• - incorporate tagline "where shine counts" (this tagline can be in a serif or sans serif font as long as it is complimentary to the overall design.
Nice to have
• - Premium elements with a clean design
Should not have
• - Please omit cartoon or whimsical like designs, think premium.
• - Colours should not stray from the pallet of the provided logo.

```html
<!DOCTYPE html>
<html lang="en">
<head>
<meta charset="utf-8">
<title>Brightvale Inc. Business Card</title>
<link href="https://fonts.googleapis.com/css2?family=Montserrat:wght@600&family=Roboto:wght@300;400;500&display=swap" rel="stylesheet">
<style>
  :root {
    --page: #e9e9e7;
    --card: #050708;
    --card-tint: #06171a;
    --teal: #14b2b5;
    --navy: #1e4a78;
    --text-light: #b8bcbf;
    --divider: #9aa0a4;
  }
  html, body {
    margin: 0;
    padding: 0;
    width: 1200px;
    height: 1200px;
    overflow: hidden;
    background: var(--page);
  }
  .canvas {
    position: relative;
    width: 1200px;
    height: 1200px;
  }
  .card {
    position: absolute;
    width: 686px;
    height: 392px;
    background: radial-gradient(ellipse 60% 80% at 60% 30%, var(--card-tint), var(--card) 70%);
    overflow: hidden;
    box-shadow: 0 6px 14px rgba(0,0,0,0.25);
  }
  .card--contact { left: 200px; top: 151px; }
  .card--brand { left: 346px; top: 624px; }
  .card__band {
    position: absolute;
    left: 0; right: 0; bottom: 0;
    height: 22px;
    background: linear-gradient(90deg, var(--navy), var(--teal) 50%, var(--navy));
  }
  .person {
    position: absolute;
    right: calc(686px - 270px);
    top: 164px;
    text-align: right;
  }
  .person__name {
    font-family: "Montserrat", sans-serif;
    font-weight: 600;
    font-size: 31px;
    color: var(--teal);
    margin: 0;
    line-height: 1;
    letter-spacing: -0.5px;
  }
  .person__role {
    font-family: "Roboto", sans-serif;
    font-weight: 300;
    font-size: 17px;
    color: var(--text-light);
    margin: 10px 0 0;
  }
  .divider {
    position: absolute;
    left: 290px;
    top: 150px;
    width: 1px;
    height: 92px;
    background: var(--divider);
  }
  .contact-list {
    position: absolute;
    left: 308px;
    top: 155px;
    margin: 0;
    padding: 0;
    list-style: none;
    font-family: "Roboto", sans-serif;
    font-weight: 300;
    font-size: 19px;
    color: var(--text-light);
  }
  .contact-list li {
    display: flex;
    align-items: center;
    gap: 7px;
    height: 28.5px;
  }
  .contact-list svg { width: 15px; height: 15px; flex: none; }
  .brand {
    position: absolute;
    left: 0; right: 0;
    top: 160px;
    text-align: center;
  }
  .brand__name {
    display: inline-flex;
    align-items: center;
    gap: 12px;
    font-family: "Roboto", sans-serif;
    font-weight: 500;
    font-size: 44px;
    color: var(--teal);
    line-height: 1;
    margin: 0;
    letter-spacing: -0.5px;
  }
  .brand__dot {
    width: 30px; height: 30px;
    border-radius: 50%;
    background: var(--teal);
  }
  .brand__tagline {
    font-family: "Roboto", sans-serif;
    font-weight: 400;
    font-size: 19px;
    letter-spacing: 1px;
    color: var(--teal);
    margin: 10px 0 0;
  }
</style>
</head>
<body>
<main class="canvas">
  <section class="card card--contact" aria-label="Business card, contact side">
    <div class="person">
      <p class="person__name">JANE HOLLOWAY</p>
      <p class="person__role">Director</p>
    </div>
    <div class="divider"></div>
    <ul class="contact-list">
      <li>
        <svg viewBox="0 0 16 16" aria-hidden="true"><path fill="#b8bcbf" d="M3.6 1.5l2.3 2.6-1.3 1.6c.9 2 2.4 3.6 4.4 4.6l1.6-1.3 2.7 2.2-1.2 2.3C7 13.2 2.8 9 1.5 3z"/></svg>
        555-014-2738
      </li>
      <li>
        <svg viewBox="0 0 16 16" aria-hidden="true"><circle cx="8" cy="8" r="6.5" fill="none" stroke="#b8bcbf" stroke-width="1.6"/><path d="M1.5 8h13M8 1.5c-3 3.5-3 9.5 0 13M8 1.5c3 3.5 3 9.5 0 13" fill="none" stroke="#b8bcbf" stroke-width="1.2"/></svg>
        www.thebrightvale.ca
      </li>
      <li>
        <svg viewBox="0 0 16 16" aria-hidden="true"><rect x="1" y="3.5" width="14" height="9.5" rx="1" fill="#b8bcbf"/><path d="M1.5 4l6.5 5 6.5-5" fill="none" stroke="#050708" stroke-width="1"/></svg>
        info@brightvalecare.ca
      </li>
    </ul>
    <div class="card__band"></div>
  </section>

  <section class="card card--brand" aria-label="Business card, brand side">
    <div class="brand">
      <p class="brand__name"><span class="brand__dot"></span>BRIGHTVALE INC.</p>
      <p class="brand__tagline">Where Shine Counts</p>
    </div>
    <div class="card__band"></div>
  </section>
</main>
</body>
</html>
```